New letter head for Air Conditioning business

We need a new professional letter head design to suit our new re-branded air conditioning business. Our new logo is attached

```html
<!DOCTYPE html>
<html lang="en">
<head>
<meta charset="utf-8">
<title>Norvent Letterhead</title>
<link href="https://fonts.googleapis.com/css2?family=PT+Sans:wght@400;700&family=Arimo:wght@400;700&display=swap" rel="stylesheet">
<style>
  :root {
    --backdrop: #e6dccd;
    --paper: #eeedee;
    --ink: #1f1f1f;
    --brand-dark: #2a2a2a;
    --brand-green: #4aa564;
    --brand-red: #d9503f;
    --stamp: #5bb8c4;
    --signature: #2d2a5a;
  }
  html, body {
    margin: 0;
    padding: 0;
    width: 1200px;
    height: 1013px;
    overflow: hidden;
    background: var(--backdrop);
  }
  .letterhead {
    position: absolute;
    left: 260px;
    top: 26px;
    width: 680px;
    height: 960px;
    background: var(--paper);
    box-shadow: 0 4px 14px rgba(0,0,0,0.18);
    font-family: "PT Sans", sans-serif;
    color: var(--ink);
    overflow: hidden;
  }
  .brand {
    position: absolute;
    left: 49px;
    top: 56px;
    display: flex;
    align-items: center;
    gap: 12px;
  }
  .brand-dot {
    width: 40px;
    height: 40px;
    border-radius: 50%;
    background: var(--brand-green);
  }
  .brand-name {
    font-family: "PT Sans", sans-serif;
    font-weight: 700;
    font-size: 27px;
    letter-spacing: 3px;
    line-height: 1;
    color: var(--brand-dark);
  }
  .brand-tagline {
    margin-top: 3px;
    font-family: "Arimo", sans-serif;
    font-weight: 700;
    font-size: 5.6px;
    letter-spacing: 1.1px;
    color: var(--brand-green);
  }
  .letter-body {
    position: absolute;
    left: 47px;
    top: 202px;
    width: 579px;
    font-size: 12.6px;
    line-height: 16.4px;
  }
  .letter-body p {
    margin: 0 0 16.4px;
    text-align: justify;
    hyphens: auto;
  }
  .signature {
    position: absolute;
    left: 52px;
    top: 695px;
    width: 76px;
    height: 54px;
    background: linear-gradient(135deg, rgba(45,42,90,0.15), rgba(45,42,90,0.05));
    border-radius: 4px;
  }
  .company-stamp {
    position: absolute;
    left: 117px;
    top: 681px;
    width: 68px;
    height: 68px;
    border: 3px solid var(--stamp);
    border-radius: 50%;
    opacity: 0.8;
  }
  .footer-rule {
    position: absolute;
    left: 141px;
    top: 897px;
    width: 484px;
    height: 1.5px;
    background: var(--brand-red);
  }
  .footer-contact {
    position: absolute;
    left: 141px;
    top: 908px;
    font-family: "Arimo", sans-serif;
    font-size: 8.5px;
    line-height: 12px;
    color: var(--brand-dark);
  }
  .contact-line {
    display: flex;
    align-items: center;
    gap: 6px;
  }
  .contact-line svg { width: 7px; height: 7px; }
  .contact-gap { height: 3px; }
</style>
</head>
<body>
  <main class="letterhead">
    <header class="brand">
      <div class="brand-dot"></div>
      <div>
        <div class="brand-name">NORVENT</div>
        <div class="brand-tagline">AIR CONDITIONING &amp; REFRIGERATION</div>
      </div>
    </header>

    <section class="letter-body">
      <p>Dear Someone Somebody,</p>
      <p>Lorem ipsum dolor sit amet, consectetuer adipiscing elit. Praesent mattis eros a tellus. Quisque leo tortor, commodo id, dapibus et, lacinia et, justo. Ut urna sapien, dictum eu, cursus vel, consectetuer tincidunt, eros. Etiam in libero. Etiam tempor. Maecenas ligula felis, commodo eget, scelerisque id, suscipit nec, odio. Vivamus commodo, magna in mollis feugiat, felis nisl dapibus dolor, eu blandit orci nulla in orci. Cras felis ipsum, mollis at, semper et, tincidunt id, ipsum. Ut consectetuer elit nec elit. Cras luctus molestie ligula. In gravida tempor nunc.</p>
      <p>Curabitur nisl ligula, pulvinar et, volutpat non, porta a, ipsum. Donec tristique ante at est. Pellentesque volutpat est non diam. Aenean vel velit. Suspendisse facilisis nisl et massa. Mauris nec erat. Pellentesque luctus arcu ut dui. Proin suscipit lorem id augue. Maecenas eget ipsum nec orci convallis viverra. Suspendisse potenti. Donec sed enim. Ut et turpis. Ut mattis enim nec nisl. Ut quam. Pellentesque lobortis vehicula risus.</p>
      <p>Etiam massa erat, tempor et, elementum fringilla, pellentesque ac, odio. Cras sed felis. Aliquam erat volutpat. Etiam tristique. Donec pellentesque, nulla semper adipiscing faucibus, nibh augue semper sapien, eget feugiat dui massa et urna. Nullam ac arcu. Quisque interdum. Morbi tristique sagittis arcu. Phasellus euismod ante eget risus. Nam convallis rutrum augue. Pellentesque placerat ultrices tellus.</p>
      <p>Ut lacinia. Sed aliquet diam at odio. Nunc ultrices pretium urna. Sed risus velit, nonummy eget, suscipit at, sagittis in, tortor. Quisque risus. Duis porta. Nunc blandit, augue et nonummy ultrices, lacus justo tincidunt nibh, eu vestibulum turpis metus iaculis ipsum. Morbi neque. Quisque augue. Etiam eleifend rhoncus metus. Aliquam auctor libero non nisi.</p>
      <p>Your Sincerely,<br>Marcus Ellery.</p>
    </section>

    <div class="signature" role="img" aria-label="Handwritten signature of the sender"></div>
    <div class="company-stamp" role="img" aria-label="Company rubber stamp"></div>

    <div class="footer-rule"></div>
    <footer class="footer-contact">
      <div>48 Linden Park Drive, Unit 12</div>
      <div>Floor 2, Fairhaven, GA 30412</div>
      <div class="contact-gap"></div>
      <div class="contact-line">
        <svg viewBox="0 0 10 10" aria-hidden="true"><path d="M2 1 L4 1 L4.6 3.4 L3.4 4.2 Q4.4 6 6 6.8 L6.8 5.6 L9 6.2 L9 8.4 Q9 9 8.2 9 Q1 8.4 1 1.8 Q1 1 2 1 Z" fill="var(--brand-green)"/></svg>
        <span>014 220 5871</span>
      </div>
      <div class="contact-line">
        <svg viewBox="0 0 10 10" aria-hidden="true"><circle cx="5" cy="5" r="4.5" fill="var(--brand-green)"/><path d="M0.5 5 H9.5 M5 0.5 Q2.5 5 5 9.5 M5 0.5 Q7.5 5 5 9.5" stroke="#fff" stroke-width="0.8" fill="none"/></svg>
        <span>www.norventclimate.com</span>
      </div>
    </footer>
  </main>
</body>
</html>
```